Tech business card design

We need an amazing business card design for our new business 'Brakka' a marketing tech startup based in Sydney, Australia. We provide an online marketplace for businesses to search and buy advertising media, connect with service providers and learn more about marketing. We wish to communicate 'cool tech', reliability and professionalism and design based around our logo.

Target Market(s)

Business Owners

Contact Information for Business Card

Name
Position
Email Address
Website
Phone Number

Font styles to use
Other font styles liked:
• Avenir & Avenir Next

Colors

Designer to choose colors to be used in the design.

```html
<!DOCTYPE html>
<html lang="en">
<head>
<meta charset="utf-8">
<title>Brakka business card</title>
<link href="https://fonts.googleapis.com/css2?family=Saira:wght@400;600;800&display=swap" rel="stylesheet">
<style>
  :root {
    --backdrop: #ececec;
    --navy: #2a2450;
    --navy-soft: #3a3466;
    --paper: #f3f3f4;
    --paper-tone: #e3e2ea;
    --ink: #231e47;
    --ink-soft: #3b3a4a;
    --white: #ffffff;
  }
  html, body {
    margin: 0;
    width: 1200px;
    height: 800px;
    overflow: hidden;
    background: var(--backdrop);
  }
  .canvas {
    position: relative;
    width: 1200px;
    height: 800px;
    font-family: "Saira", sans-serif;
  }
  .card {
    position: absolute;
    top: 278px;
    width: 418px;
    height: 240px;
    overflow: hidden;
  }
  .card--front { left: 142px; background: var(--navy); }
  .card--back  { left: 638px; background: var(--paper); }

  .card__pattern {
    position: absolute;
    inset: 0;
  }
  .card--front .card__pattern {
    background: radial-gradient(ellipse 70% 45% at 55% 55%, var(--navy-soft), transparent 75%);
  }
  .card--back .card__pattern {
    background: radial-gradient(ellipse 60% 50% at 60% 55%, var(--paper-tone), transparent 75%);
  }

  .wordmark {
    position: absolute;
    font-weight: 800;
    font-size: 50px;
    line-height: 1;
    letter-spacing: -0.5px;
  }
  .wordmark sup {
    font-size: 7px;
    font-weight: 800;
    vertical-align: baseline;
    margin-left: 2px;
  }
  .card--front .wordmark {
    left: 0; right: 0;
    top: 92px;
    text-align: center;
    color: var(--white);
  }
  .card--back .wordmark {
    left: 45px;
    top: 95px;
    color: var(--ink);
  }

  .identity {
    position: absolute;
    left: 225px;
    top: 45px;
    line-height: 1.1;
  }
  .identity__name {
    font-weight: 600;
    font-size: 15px;
    color: var(--ink);
  }
  .identity__role {
    font-size: 14px;
    color: var(--ink-soft);
  }
  .contact {
    position: absolute;
    left: 225px;
    top: 146px;
    margin: 0;
    padding: 0;
    list-style: none;
    font-size: 14.5px;
    line-height: 17px;
    color: var(--ink-soft);
  }
</style>
</head>
<body>
<div class="canvas">
  <section class="card card--front">
    <div class="card__pattern" role="img" aria-label="Faint network of connected dots with flowing wave lines"></div>
    <div class="wordmark">Brakka<sup>TM</sup></div>
  </section>

  <section class="card card--back">
    <div class="card__pattern" role="img" aria-label="Light grey network of connected dots with flowing wave lines"></div>
    <div class="wordmark">Brakka<sup>TM</sup></div>
    <div class="identity">
      <div class="identity__name">Lena Marsh</div>
      <div class="identity__role">manager</div>
    </div>
    <ul class="contact">
      <li>012 345 6789</li>
      <li>your@email.com</li>
      <li>www.website.com</li>
    </ul>
  </section>
</div>
</body>
</html>
```